Website Design for Videographer

I am looking to update my website - www.bennloxwood.com. I am a wedding videographer who specialises in natural and documentary videography.

The website will be built by my designer using the Wordpress Brightframe framework.

Requirements;
I want the website to have a clean white look mixed in with video footage.
Needs to be classy. At the moment my website uses a lot of Gold. On the new look I DO NOT want gold.

Need a web and mobile design for the following 12 pages;

* Home page (need to have example videos and text)
* About (this is about me and my service)
* Videos (examples of my work)
* Testimonials
* Packages
* Contact
* Content (this is to show social media content that I am making in a vertical format and advertise this service).
* Blog (index page for blog)
* Blog pages (individual pages for blog content)
* Wedding Venues Index Page (https://bennloxwood.com/north-east-wedding-venues/)
* Individual venue pages (https://bennloxwood.com/north-east-wedding-venues/marrow-ridge-lodge-wedding-videos/) - Needs to show videos, photos, text as is on the current page.
* Venue Tours (https://bennloxwood.com/wedding-venue-tours/)

My current logo is attached however on the website I want to go for a black and white style for it.

Example styles I like however must not be copied.
https://dovimellor.co.uk/about/
https://tidewhistle.co.uk/ (if done in white)
https://plumquartzreels.co.uk/

Target Market(s)

Couples getting married aged 25-35

Industry/Entity Type

Weddings

Number of Pages Required

5+ page

Font styles to use
Sans Serif

Requirements
Must have
• A classy look, black and white, use videos and photos.
Should not have
• Gold colour

```html
<!DOCTYPE html>
<html lang="en">
<head>
<meta charset="utf-8">
<title>Benn Loxwood – Landing Page Mobile View</title>
<link rel="stylesheet" href="https://fonts.googleapis.com/css2?family=Bebas+Neue&family=Montserrat:wght@400;500;600&family=Quicksand:wght@400;500&display=swap">
<style>
  :root {
    --canvas: #161616;
    --ink: #0b0b0b;
    --white: #ffffff;
    --text-grey: #6d6d6d;
    --heading: #3a3a3a;
    --play-blue: #2ea3e6;
    --card-dark: rgba(40, 36, 32, 0.82);
    --field-border: #d9d9d9;
  }
  * { box-sizing: border-box; margin: 0; padding: 0; }
  html, body { width: 1200px; height: 853px; overflow: hidden; }
  body {
    background: var(--canvas);
    font-family: "Quicksand", sans-serif;
    position: relative;
  }
  .sheet-title {
    position: absolute; left: 67px; top: 40px; width: 200px;
    text-align: center; color: var(--white);
    font-family: "Montserrat", sans-serif;
  }
  .sheet-title .eyebrow { font-size: 11px; letter-spacing: 2px; font-weight: 500; }
  .sheet-title .main { font-size: 14px; letter-spacing: 2.5px; font-weight: 600; margin-top: 9px; }
  .sheet-title .sub { font-size: 11px; letter-spacing: 2px; margin-top: 8px; }

  .screen { position: absolute; width: 263px; background: var(--white); overflow: hidden; }
  .screen-1 { left: 34px; top: 139px; height: 714px; border-radius: 14px 14px 0 0; }
  .screen-2 { left: 323px; top: 0; height: 853px; }
  .screen-3 { left: 612px; top: 0; height: 853px; }
  .screen-4 { left: 902px; top: 0; height: 853px; background: var(--ink); }

  .abs { position: absolute; }
  .media { position: absolute; }
  .display { font-family: "Bebas Neue", sans-serif; letter-spacing: 0.5px; text-align: center; font-weight: 400; }
  .copy { font-size: 10.5px; line-height: 14px; color: var(--text-grey); text-align: center; }
  .btn {
    position: absolute; background: var(--ink); color: var(--white);
    font-family: "Montserrat", sans-serif; font-size: 10.5px;
    display: flex; align-items: center; justify-content: center; border-radius: 7px;
  }
  .play {
    position: absolute; background: var(--play-blue); border-radius: 3px;
    display: flex; align-items: center; justify-content: center;
  }

  /* screen 1 */
  .hero-photo {
    left: 0; top: 0; width: 263px; height: 327px;
    background: linear-gradient(180deg, #2a2420 0%, #6d5e56 35%, #8f857f 62%, #d8d5d3 85%, #ffffff 100%);
  }
  .nav-menu { left: 15px; top: 15px; }
  .nav-brand {
    left: 80px; top: 15px; width: 103px; text-align: center; color: var(--white);
    font-family: "Quicksand", sans-serif; font-size: 6px; font-weight: 500;
  }
  .nav-enquire { left: 212px; top: 8px; width: 44px; height: 20px; font-size: 7px; border-radius: 5px; }
  .hero-title {
    left: 0; top: 153px; width: 263px; color: var(--white); font-size: 18px; letter-spacing: 1.2px;
    text-shadow: 0 0 2px rgba(0,0,0,0.7);
  }
  .hero-sub {
    left: 0; top: 175px; width: 263px; color: var(--white); font-size: 10px; letter-spacing: 2.5px;
    text-shadow: 0 0 2px rgba(0,0,0,0.7);
  }
  .hero-cta { left: 80px; top: 208px; width: 103px; height: 29px; }
  .intro-title { left: 0; top: 393px; width: 263px; color: var(--heading); font-size: 16px; }
  .intro-copy { left: 14px; top: 423px; width: 235px; }
  .intro-video {
    left: 12px; top: 479px; width: 239px; height: 240px; border-radius: 8px;
    background: linear-gradient(160deg, #5c4c3c 0%, #7b6a55 40%, #3f352d 100%);
  }
  .intro-play { left: 87px; top: 157px; width: 65px; height: 39px; }

  /* screen 2 */
  .feature-video {
    left: 12px; top: 0; width: 239px; height: 172px; border-radius: 0 0 8px 8px;
    background: linear-gradient(180deg, #6e625a 0%, #938982 55%, #c9c2bb 100%);
  }
  .feature-play { left: 88px; top: 0; width: 65px; height: 17px; border-radius: 0 0 3px 3px; }
  .story-copy-1 { left: 16px; top: 188px; width: 231px; }
  .story-copy-2 { left: 18px; top: 259px; width: 227px; }
  .reel-band {
    left: 0; top: 391px; width: 263px; height: 147px;
    background: radial-gradient(ellipse at 50% 40%, #3b3836 0%, #121212 55%, #050505 100%);
  }
  .reel-play { left: 118px; top: 66px; width: 28px; height: 16px; }
  .carousel { left: 0; top: 557px; width: 263px; height: 26px; }
  .view-all {
    left: 0; top: 602px; width: 263px; text-align: center; color: #8a8a8a;
    font-size: 13px; text-decoration: underline;
  }
  .awards-band {
    left: 0; top: 692px; width: 263px; height: 161px;
    background: linear-gradient(180deg, #ffffff 0%, #d9cfc4 30%, #a89580 100%);
  }
  .awards-card {
    left: 12px; top: 749px; width: 238px; height: 110px; border-radius: 9px;
    background: linear-gradient(180deg, #3f352c 0%, #2b241e 100%);
  }
  .awards-title { left: 0; top: 36px; width: 238px; color: var(--white); font-size: 13px; }
  .awards-badge {
    left: 46px; top: 84px; width: 135px; height: 30px; border-radius: 5px 5px 0 0;
    background: linear-gradient(90deg, #3a3a3a, #1c1c1c);
  }

  /* screen 3 */
  .review-photo {
    left: 0; top: 0; width: 263px; height: 160px;
    background: linear-gradient(180deg, #4a4038 0%, #6a5f55 60%, #ffffff 100%);
  }
  .review-card { left: 12px; top: 0; width: 238px; height: 103px; border-radius: 0 0 8px 8px; background: var(--card-dark); }
  .review-text {
    left: 13px; top: -6px; width: 212px; color: #eeeeee; font-size: 10px; line-height: 14px; text-align: justify;
  }
  .scene-road {
    left: 12px; top: 288px; width: 161px; height: 203px; border-radius: 5px;
    background: linear-gradient(180deg, #eef0ef 0%, #eef0ef 38%, #8a9a6e 52%, #6f7762 75%, #8d8f8c 100%);
  }
  .scene-couple {
    left: 95px; top: 252px; width: 157px; height: 195px; border-radius: 5px;
    background: linear-gradient(170deg, #6e6459 0%, #a79c91 40%, #d5d2cf 70%, #b9b7b7 100%);
  }
  .day-title { left: 0; top: 535px; width: 263px; color: var(--heading); font-size: 13px; line-height: 19px; }
  .day-copy-1 { left: 12px; top: 599px; width: 239px; text-align: justify; }
  .day-copy-2 { left: 12px; top: 641px; width: 239px; text-align: justify; }
  .day-cta { left: 80px; top: 727px; width: 103px; height: 31px; }
  .next-band { left: 12px; top: 844px; width: 239px; height: 12px; background: var(--ink); border-radius: 6px 6px 0 0; }

  /* screen 4 */
  .contact-photo {
    left: 0; top: 0; width: 263px; height: 515px;
    background: linear-gradient(180deg, #2b2a2e 0%, #3b3a45 45%, #4b4a62 80%, #2f2e3a 100%);
  }
  .contact-card { left: 12px; top: 35px; width: 240px; height: 412px; border-radius: 9px; background: rgba(28, 28, 28, 0.82); }
  .contact-title { left: 0; top: 64px; width: 263px; color: var(--white); font-size: 14px; }
  .field {
    position: absolute; left: 25px; width: 213px; height: 29px; background: var(--white);
    border: 1px solid var(--field-border); font-size: 6px; color: #8c8c8c;
    padding: 0 10px; display: flex; align-items: center;
  }
  .field.tall { height: 39px; align-items: flex-start; padding-top: 11px; }
  .send-btn { left: 177px; top: 398px; width: 61px; height: 37px; font-size: 11px; }
  .footer-brand {
    left: 0; top: 600px; width: 263px; display: flex; align-items: center; justify-content: center; gap: 8px;
    color: var(--white); font-family: "Quicksand", sans-serif; font-weight: 500; font-size: 16px;
  }
  .footer-brand .mark { width: 10px; height: 10px; background: var(--white); }
  .footer-label { left: 0; top: 708px; width: 263px; color: var(--white); font-size: 11px; letter-spacing: 0.5px; }
  .footer-line {
    left: 0; width: 263px; text-align: center; color: #e6e6e6;
    font-family: "Montserrat", sans-serif; font-size: 8px;
  }
  .energy-badge { left: 54px; top: 797px; width: 155px; height: 36px; background: var(--white); border-radius: 4px; }
</style>
</head>
<body>

  <header class="sheet-title">
    <div class="eyebrow">BENN LOXWOOD</div>
    <div class="main">LANDING PAGE</div>
    <div class="sub">MOBILE VIEW</div>
  </header>

  <section class="screen screen-1">
    <div class="media hero-photo" role="img" aria-label="Bride and groom smiling under falling confetti"></div>
    <svg class="abs nav-menu" width="12" height="9" viewBox="0 0 12 9">
      <rect y="0" width="12" height="1.5" fill="#fff"/><rect y="3.7" width="12" height="1.5" fill="#fff"/><rect y="7.5" width="12" height="1.5" fill="#fff"/>
    </svg>
    <div class="abs nav-brand">Benn Loxwood</div>
    <div class="btn nav-enquire">Enquire</div>
    <h1 class="abs display hero-title">NORTH EAST WEDDING VIDEOGRAPHER</h1>
    <div class="abs display hero-sub">BENN LOXWOOD</div>
    <div class="btn hero-cta">Check Availibilty</div>

    <h2 class="abs display intro-title">STUNNING NORTH EAST WEDDING FILMS</h2>
    <p class="abs copy intro-copy">A trusted and acclaimed North East wedding videographer who has more than 25 years of videography experience.</p>
    <div class="media intro-video" role="img" aria-label="Candlelit barn wedding ceremony with couple at the altar">
      <div class="play intro-play">
        <svg width="18" height="18" viewBox="0 0 18 18"><path d="M4 2 L16 9 L4 16 Z" fill="#fff"/></svg>
      </div>
    </div>
  </section>

  <section class="screen screen-2">
    <div class="media feature-video" role="img" aria-label="Couple walking down the aisle between guests">
      <div class="play feature-play">
        <svg width="10" height="10" viewBox="0 0 10 10"><path d="M2 0 L9 5 L2 10 Z" fill="#fff"/></svg>
      </div>
    </div>
    <p class="abs copy story-copy-1">From beautiful barns and luxurious country hotels to sun-drenched Greek Islands and ancient Italian abbeys, he has filmed all kinds of unforgettable weddings.</p>
    <p class="abs copy story-copy-2">If you're looking for a highly experienced wedding videographer who focuses on your story, the "goosebump" moments and the emotions filling the room as you entertain your guests, then get in touch with Benn today.</p>

    <div class="media reel-band" role="img" aria-label="Black and white film still of a couple embracing">
      <div class="play reel-play">
        <svg width="8" height="8" viewBox="0 0 10 10"><path d="M2 0 L9 5 L2 10 Z" fill="#fff"/></svg>
      </div>
    </div>

    <svg class="abs carousel" width="263" height="26" viewBox="0 0 263 26">
      <circle cx="52" cy="13" r="12.5" fill="none" stroke="#222" stroke-width="1.2"/>
      <path d="M58 13 H46 M50 9 L46 13 L50 17" fill="none" stroke="#222" stroke-width="1.3"/>
      <circle cx="106" cy="13" r="2" fill="#ddd"/>
      <circle cx="116" cy="13" r="2" fill="#333"/>
      <circle cx="126" cy="13" r="2" fill="#ddd"/>
      <circle cx="136" cy="13" r="2" fill="#ddd"/>
      <circle cx="146" cy="13" r="2" fill="#ddd"/>
      <circle cx="156" cy="13" r="2" fill="#ddd"/>
      <circle cx="211" cy="13" r="12.5" fill="none" stroke="#222" stroke-width="1.2"/>
      <path d="M205 13 H217 M213 9 L217 13 L213 17" fill="none" stroke="#222" stroke-width="1.3"/>
    </svg>
    <div class="abs view-all">view all</div>

    <div class="media awards-band" role="img" aria-label="Festoon lights strung over a reception venue"></div>
    <div class="abs awards-card">
      <h3 class="abs display awards-title">VEILBOUND WEDDING AWARDS 2024 WINNER</h3>
      <div class="abs awards-badge"></div>
    </div>
  </section>

  <section class="screen screen-3">
    <div class="media review-photo" role="img" aria-label="Wedding venue interior behind the review"></div>
    <div class="abs review-card">
      <p class="abs review-text">honour of working with makes it even more noteworthy. What really sealed the deal for me on this award was their satisfaction and the memories we've made together.</p>
    </div>

    <div class="media scene-road" role="img" aria-label="Vintage wedding car on a country road"></div>
    <div class="media scene-couple" role="img" aria-label="Newlyweds walking through a shower of confetti"></div>

    <h2 class="abs display day-title">YOUR WEDDING DAY IS<br>THE MOST IMPORTANTDAY OF YOUR LIFE...</h2>
    <p class="abs copy day-copy-1">The celebration of your love story... and you'll want to remember it for the rest of your lives.</p>
    <p class="abs copy day-copy-2">Your wedding film is the best way to keep this day alive forever ... a newlywed's gift that keeps giving ... an infinite reminder of those special moments and memories.</p>
    <div class="btn day-cta">Check Availibilty</div>
    <div class="abs next-band"></div>
  </section>

  <section class="screen screen-4">
    <div class="media contact-photo" role="img" aria-label="Reception guests dancing under evening lights"></div>
    <div class="abs contact-card"></div>
    <h2 class="abs display contact-title">GET IN TOUCH</h2>
    <div class="field" style="top:107px">Name</div>
    <div class="field" style="top:147px">Email Address</div>
    <div class="field" style="top:188px">Date of Wedding</div>
    <div class="field" style="top:228px">Location of Wedding</div>
    <div class="field tall" style="top:268px">Tell me a bit more about how you envisage your wedding day...</div>
    <div class="field" style="top:318px">Tell me more about you and your story...</div>
    <div class="field" style="top:358px">What do you like about my films?</div>
    <div class="btn send-btn">Send</div>

    <div class="abs footer-brand"><span class="mark"></span><span>Benn Loxwood</span></div>
    <h3 class="abs display footer-label">CONTACT</h3>
    <div class="abs footer-line" style="top:741px">07700 900 318</div>
    <div class="abs footer-line" style="top:766px">films@bennloxwood.com</div>
    <div class="abs energy-badge"></div>
  </section>

</body>
</html>
```